" 738 " PACKAGING FOR AUTOMOTIVE SPAREPARTS PRODUCT

We need a zipped plastic packaging design for our product (i attached plastic packaging sample from another product). The plastic size is 40cm (length) * 30cm (width) with zipped on upside.

Our product is rubber parts for car suspension application. The brand is 738 and the slogan is 738 ORIGINAL PARTS ( see attached file).

We prefer the design use mostly red color (same color as our logo) and combine with other attracting color and it is on your control.
I have included a picture of packaging box that we currently use.

On the front side of the plastic packaging should have a view window that can view and see through the product inside the packaging.

The color and the design is on your control.
Updates

Project Deadline Extended
Reason: Hi I extend the deadline, create your Best design..

Target Market(s)

All customers, car workshop, retailer and user.

Industry/Entity Type

Automotive

Requirements
Must have
• - A space for labeling on front side of the packaging. (label size 4cm (lenght) * 7cm (width).
• - Should have the Pictures of our product on the packaging. I have included some pictures of our product, You can choose and put some of the pictures on the packaging.
• - The design should can communicate HIGH QUALITY PARTS.
Nice to have
• - Have some Blue print or silhouette (with a bit transparancy) of car spareparts item or workshop tool kit on the design.

```html
<!DOCTYPE html>
<html lang="en">
<head>
<meta charset="utf-8">
<title>738 Original Parts – Pouch Front</title>
<link href="https://fonts.googleapis.com/css2?family=Poppins:wght@600;700&family=Saira+Condensed:wght@400&display=swap" rel="stylesheet">
<style>
  :root {
    --backdrop: #ecebd8;
    --pouch-red: #b8101a;
    --pouch-red-deep: #7a0a10;
    --window-red: #c3242b;
    --window-red-light: #e0474a;
    --band-red: #e0333a;
    --charcoal: #3a3a3c;
    --gear-grey: #4a4a4c;
    --ink-light: #f4e9e6;
    --watermark-coral: #f27a74;
  }
  html, body {
    margin: 0;
    padding: 0;
    width: 1200px;
    height: 1020px;
    overflow: hidden;
    background: var(--backdrop);
  }
  .canvas {
    display: block;
    width: 1200px;
    height: 1020px;
  }
  .brand-name {
    font-family: "Poppins", sans-serif;
    font-weight: 700;
    fill: var(--ink-light);
  }
  .brand-tagline {
    font-family: "Saira Condensed", sans-serif;
    font-weight: 400;
    fill: var(--ink-light);
  }
  .band-headline,
  .band-subline {
    font-family: "Poppins", sans-serif;
    font-weight: 700;
    fill: var(--ink-light);
  }
  .brand-watermark {
    font-family: "Poppins", sans-serif;
    font-weight: 700;
    fill: var(--watermark-coral);
    opacity: 0.6;
  }
</style>
</head>
<body>
<svg class="canvas" viewBox="0 0 1200 1020" xmlns="http://www.w3.org/2000/svg">
  <defs>
    <linearGradient id="pouchShade" x1="0" x2="1" y1="0" y2="0">
      <stop offset="0" stop-color="var(--pouch-red-deep)"/>
      <stop offset="0.5" stop-color="var(--pouch-red)"/>
      <stop offset="1" stop-color="var(--pouch-red-deep)"/>
    </linearGradient>
    <linearGradient id="windowShade" x1="0" x2="1" y1="0" y2="1">
      <stop offset="0" stop-color="#a81a22"/>
      <stop offset="0.55" stop-color="var(--window-red-light)"/>
      <stop offset="1" stop-color="var(--window-red)"/>
    </linearGradient>
    <clipPath id="windowClip">
      <path d="M362 165 H844 Q864 165 864 185 V905 Q740 945 600 945 Q470 945 342 930 V185 Q342 165 362 165 Z"/>
    </clipPath>
  </defs>

  <!-- pouch body -->
  <g class="pouch">
    <path class="pouch-body" fill="url(#pouchShade)"
      d="M312 80 H888 Q900 80 900 92 V174 A9 9 0 0 0 900 192 V915 Q600 955 300 915 V192 A9 9 0 0 0 300 174 V92 Q300 80 312 80 Z"/>
    <rect class="zip-seal" x="300" y="100" width="600" height="4" fill="var(--pouch-red-deep)"/>
    <rect class="zip-seal" x="300" y="112" width="600" height="3" fill="var(--pouch-red-deep)"/>
  </g>

  <!-- view window -->
  <g class="view-window" clip-path="url(#windowClip)">
    <rect x="342" y="165" width="522" height="780" fill="url(#windowShade)"/>

    <rect class="gear-artwork" x="580" y="200" width="284" height="420" fill="var(--gear-grey)" opacity="0.55"
      role="img" aria-label="Silhouettes of interlocking gears"/>

    <path class="lower-dark-panel" d="M560 760 L864 600 V945 H560 Z" fill="var(--charcoal)"/>
    <path class="accent-stripe" d="M342 690 L470 660 L470 680 L342 712 Z" fill="var(--band-red)"/>

    <path class="slogan-band" d="M342 718 L864 560 V640 L342 800 Z" fill="var(--band-red)"/>
    <path class="lower-red-sweep" d="M342 830 L864 660 V700 L560 800 L560 945 H342 Z" fill="var(--band-red)"/>

    <text class="band-headline" x="354" y="745" font-size="24" transform="rotate(-17 354 745)">HIGH QUALITY AUTO PARTS</text>
    <text class="band-subline" x="440" y="765" font-size="21" transform="rotate(-17 440 765)">738 Original Parts</text>

    <text class="brand-watermark" x="475" y="905" font-size="110" transform="rotate(-10 475 905)">738</text>
  </g>

  <!-- brand -->
  <g class="brand">
    <circle cx="378" cy="266" r="12" fill="var(--ink-light)"/>
    <text class="brand-name" x="400" y="284" font-size="52" transform="rotate(-12 400 284)">738</text>
    <text class="brand-tagline" x="375" y="395" font-size="26" transform="rotate(4 375 395)">738 Original Parts</text>
  </g>
</svg>
</body>
</html>
```